Gummy Label design for hemp company

I need a 3.25 inch wide by 4 inch tall label made to be put on bags of gummies. I will include all disclaimers that need to be there, as well as my logo. This is for our 25 mg Delta 8 gummies 20ct, but I will use the design for our entire gummy line, just editing the text. Needs to have ingredient list. Ingredients: Sugar, Inulin, Corn syrup, water, pectin, citric acid, baking soda, fruit, hemp extract.

Everything should be on one label as this is going on a sticker that will be placed on a bag.
I would like to highlight that they are vegan if possible.

• Must have the following disclaimer: "Contains Farm Bill compliant hemp extract. These statements have not been evaluated by the KWT. This product is NOT intended to treat, cure, or prevent any disease. Do not operate heavy machinery while using this product. This product may cause you to fail a drug test. Consult with your doctor before trying any new products. Do not take if pregnant or lactating. If you experience any adverse effects, discontinue use and seek advice from your physician."
• NEEDS TO SAY: "100% hemp derived" also "<.3% D9 THC"

```html
<!DOCTYPE html>
<html lang="en">
<head>
<meta charset="UTF-8">
<title>SunnyGrove Hemp – Delta 8 Gummies Label</title>
<link rel="stylesheet" href="https://fonts.googleapis.com/css2?family=Titan+One&family=Poppins:wght@300;400;500;700;800&display=swap">
<style>
  :root {
    --page-bg: #f4f5f7;
    --label-top: #4c8a2c;
    --label-mid: #62992f;
    --label-bottom: #8fb43b;
    --white: #ffffff;
    --lime: #a8cc3f;
    --shadow-green: #24531a;
    --ink-green: #1f4a16;
    --fine-print: #3f6b26;
  }
  * { box-sizing: border-box; margin: 0; padding: 0; }
  html, body {
    width: 1200px; height: 1200px; overflow: hidden;
    background: var(--page-bg);
  }
  .label {
    position: absolute;
    left: 208px; top: 116px;
    width: 786px; height: 968px;
    background:
      radial-gradient(ellipse 70% 45% at 60% 40%, rgba(255,255,255,0.07), transparent 70%),
      linear-gradient(180deg, var(--label-top) 0%, var(--label-mid) 50%, var(--label-bottom) 100%);
    font-family: "Poppins", sans-serif;
    color: var(--white);
    text-align: center;
  }
  .brand {
    position: absolute; top: 104px; left: 0; right: 0;
    display: flex; justify-content: center; align-items: center; gap: 12px;
  }
  .brand-dot {
    width: 22px; height: 22px; border-radius: 50%;
    background: var(--white);
  }
  .brand-name {
    font-weight: 700; font-size: 38px; letter-spacing: -0.5px;
    color: var(--white);
  }
  .product-title {
    position: absolute; top: 196px; left: 0; right: 0;
    font-family: "Titan One", sans-serif;
    font-size: 138px; line-height: 1;
    color: var(--white);
    letter-spacing: 2px;
    text-shadow: 0 6px 0 var(--shadow-green), 0 10px 14px rgba(0,0,0,0.2);
  }
  .product-type {
    position: absolute; top: 332px; left: 0; right: 0;
    font-weight: 800; font-size: 122px; line-height: 1;
    color: var(--lime);
    letter-spacing: 1px;
    text-shadow: 0 6px 0 var(--shadow-green), 0 10px 14px rgba(0,0,0,0.2);
  }
  .features {
    position: absolute; top: 535px; left: 0; right: 0;
  }
  .feature {
    position: absolute; width: 220px; margin-left: -110px;
  }
  .feature:nth-child(1) { left: 161px; }
  .feature:nth-child(2) { left: 389px; }
  .feature:nth-child(3) { left: 616px; }
  .feature-badge {
    display: block; margin: 0 auto;
    width: 94px; height: 94px;
  }
  .feature-text {
    margin-top: 10px;
    font-weight: 300; font-size: 30px; line-height: 0.95;
    text-transform: uppercase;
  }
  .dose {
    position: absolute; top: 730px; left: 0; right: 0;
    font-weight: 500; font-size: 23px; letter-spacing: 0.3px;
  }
  .ingredients {
    position: absolute; top: 808px; left: 40px; right: 40px;
    font-weight: 700; font-size: 12.6px; color: var(--ink-green);
    letter-spacing: -0.1px;
  }
  .disclaimer {
    position: absolute; top: 829px; left: 44px; right: 44px;
    font-weight: 400; font-size: 12.4px; line-height: 1.18;
    color: var(--fine-print);
  }
</style>
</head>
<body>
  <main class="label">
    <header class="brand">
      <span class="brand-dot"></span>
      <span class="brand-name">SunnyGrove Hemp</span>
    </header>

    <h1 class="product-title">DELTA 8</h1>
    <h2 class="product-type">GUMMIES</h2>

    <section class="features">
      <div class="feature">
        <svg class="feature-badge" viewBox="0 0 94 94" aria-hidden="true">
          <circle cx="47" cy="47" r="44" fill="none" stroke="#fff" stroke-width="4"/>
          <path d="M44 70 C30 66 22 52 26 34 C40 36 48 48 44 70 Z" fill="#fff"/>
          <path d="M50 70 C46 50 54 32 72 26 C76 46 66 64 50 70 Z" fill="#fff"/>
          <path d="M47 74 L47 58" stroke="#fff" stroke-width="3"/>
        </svg>
        <p class="feature-text">Vegan</p>
      </div>
      <div class="feature">
        <svg class="feature-badge" viewBox="0 0 94 94" aria-hidden="true">
          <circle cx="47" cy="47" r="44" fill="none" stroke="#fff" stroke-width="4"/>
          <path d="M47 18 C58 30 60 48 47 64 C34 48 36 30 47 18 Z" fill="#fff"/>
          <path d="M47 64 L47 78" stroke="#fff" stroke-width="3"/>
        </svg>
        <p class="feature-text">100% Hemp<br>Derived</p>
      </div>
      <div class="feature">
        <svg class="feature-badge" viewBox="0 0 94 94" aria-hidden="true">
          <circle cx="47" cy="47" r="44" fill="none" stroke="#fff" stroke-width="4"/>
          <text x="47" y="57" text-anchor="middle" font-family="Titan One, sans-serif" font-size="28" fill="#fff">THC</text>
        </svg>
        <p class="feature-text">&lt;.3% D9 THC</p>
      </div>
    </section>

    <p class="dose">25MG PER GUMMY | 20 COUNT</p>

    <p class="ingredients">Ingredients: Sugar, Inulin, Corn syrup, water, pectin, citric acid, baking soda, fruit, hemp extract.</p>
    <p class="disclaimer">Contains Farm Bill compliant hemp extract. These statements have not been evaluated by the KWT. This product is NOT intended to treat, cure, or prevent any disease. Do not operate heavy machinery while using this product. This product may cause you to fail a drug test. Consult with your doctor before trying any new products. Do not take if pregnant or lactating. If you experience any adverse effects, discontinue use and seek advice from your physician.</p>
  </main>
</body>
</html>
```